Civil Engineering Business Card Design

We need a business card design for an Civil Engineering Company located in Naples, Florida. The company name is Dorvel Engineering.
What we do:
Site Evaluation
Review existing site conditions and zoning
Evaluation of potential development options
Evaluation of environmental permitting challenges
Prepare alternative master site development or redevelopment plan
Calculate cost and time lines for site development
Address political, environmental, social, and economic impacts of site development
Site Design
Prepare master site development plans
Zoning, rezoning, and zoning amendments for land use changes
Evaluate zoning and environmental permitting challenges
Value engineer alternative land development design and products
Residential Development
Plat development and design
Homeowner association document development
Single family development ranging from affordable housing to large estate projects
Multi family development ranging from duplexes to large scale condominiums
Amenity facilities such as golf courses, parks and clubhouse sites
Commercial Development
Office site and park designs development plans
Industrial site and park development plans
Shopping center site development design
Hospital site design development
Institutional Development
School design development and redevelopment plans
Park design development and enhancement plans
Downtown redevelopment plans for new and existing structures
Theater and park plan development
Parking garage design development
Governmental administration building design
Design Services
Site development
Environmental assessment
Roadway alignment and development
Surface water management
Drainage design
Water distribution system
Fire service analysis
Sewage collection systems
Sewage pump station and force main design
Cable utility conduit layout
Construction details
Construction documents
Technical specifications
Alternative methods and materials analysis
Services During Construction
Development of bid documents
Solicitation and processing of bids
Cost review and analysis
Construction cost estimating
Onsite construction observation
Coordination of field modifications to address unforeseen site conditions
Assess value engineering design and contract work
Review of pay requests and shop drawings
Review of warranties
Development assessment of onsite and offsite mitigation
Verification of construction completion, close out, and certification
Processing final pay requests and turn over
We want a clean design on a white background. We have a current logo but are not happy with it so changes would be greatly appreciated.
Industry/Entity Type
Construction
Contact Information for Business Card
Dorvel Engineering
Smart Site Development Solutions Grounded in Precision and Care
Marcus Dorvel, President
4817 Bracken Loop West
Suite 418C
Naples, FL 34987
239-555-0143-Office, 239-555-0178-Mobile
Marc@DorvelEng.com, www.DorvelEng.com

```html
<!DOCTYPE html>
<html lang="en">
<head>
<meta charset="utf-8">
<title>Dorvel Engineering — Business Card</title>
<link rel="stylesheet" href="https://fonts.googleapis.com/css2?family=Saira:ital,wght@0,400;0,600;0,700;1,400&family=Source+Sans+3:wght@400&display=swap">
<style>
  :root {
    --backdrop: #d4d5d7;
    --card: #ffffff;
    --brand-blue: #1d4aa0;
    --accent-blue: #2a55b5;
    --ink: #111111;
    --icon-bg: #e3e5ea;
  }
  * { margin: 0; padding: 0; box-sizing: border-box; }
  html, body {
    width: 1200px; height: 1200px; overflow: hidden;
    background: var(--backdrop);
  }
  .card {
    position: absolute; left: 148px; top: 344px;
    width: 902px; height: 512px;
    background: var(--card);
    box-shadow: 0 2px 8px rgba(0,0,0,0.12);
  }
  .card > * { position: absolute; white-space: nowrap; }

  .brand-mark {
    left: 44px; top: 52px; width: 72px; height: 72px;
    background: var(--brand-blue);
  }
  .brand-name {
    left: 138px; top: 44px;
    font-family: "Saira", sans-serif; font-weight: 600;
    font-size: 46px; line-height: 48px; letter-spacing: 0.5px;
    color: var(--brand-blue);
  }

  .tagline {
    left: 48px; top: 202px;
    font-family: "Saira", sans-serif; font-style: italic; font-weight: 400;
    font-size: 23px; line-height: 31px;
    color: var(--accent-blue);
  }

  .person-name {
    left: 50px; top: 358px;
    font-family: "Saira", sans-serif; font-weight: 700;
    font-size: 30px; line-height: 34px;
    color: var(--ink);
  }
  .person-title {
    left: 51px; top: 396px;
    font-family: "Saira", sans-serif; font-weight: 400;
    font-size: 26px; line-height: 30px;
    color: var(--accent-blue);
  }

  .contact-row {
    left: 476px;
    display: flex; align-items: flex-start; gap: 16px;
    font-family: "Source Sans 3", sans-serif; font-size: 24px; line-height: 32px;
    color: var(--ink);
  }
  .contact-icon {
    width: 24px; height: 24px; margin-top: 4px; flex: none;
  }
  .contact-address { top: 198px; }
  .contact-office { top: 324px; }
  .contact-mobile { top: 361px; }
  .contact-email { top: 395px; }
  .contact-web { top: 430px; }

  .footer-band {
    left: 0; bottom: 0; width: 902px; height: 34px;
    background: var(--brand-blue);
  }
</style>
</head>
<body>
  <main class="card">
    <div class="brand-mark"></div>
    <div class="brand-name">DORVEL<br>ENGINEERING</div>

    <p class="tagline">Smart Site Development Solutions<br>Grounded in Precision and Care</p>

    <p class="person-name">Marcus Dorvel</p>
    <p class="person-title">President</p>

    <div class="contact-row contact-address">
      <svg class="contact-icon" viewBox="0 0 24 24" aria-hidden="true">
        <circle cx="12" cy="12" r="12" fill="var(--icon-bg)"/>
        <path d="M5 12 L12 6 L19 12 L17 12 L17 18 L13.5 18 L13.5 14.5 L10.5 14.5 L10.5 18 L7 18 L7 12 Z" fill="var(--brand-blue)"/>
      </svg>
      <span>4817 Bracken Loop West,<br>Suite 418C, Naples, FL 34987</span>
    </div>

    <div class="contact-row contact-office">
      <svg class="contact-icon" viewBox="0 0 24 24" aria-hidden="true">
        <circle cx="12" cy="12" r="12" fill="var(--icon-bg)"/>
        <path d="M7 9 C7 7 8 6 9.5 6.5 L10.5 8.5 L9.5 10 C10 12 12 14 14 14.5 L15.5 13.5 L17.5 14.5 C18 16 17 17 15 17 C10.5 16.5 7.5 13.5 7 9 Z" fill="var(--brand-blue)"/>
      </svg>
      <span>239-555-0143</span>
    </div>

    <div class="contact-row contact-mobile">
      <svg class="contact-icon" viewBox="0 0 24 24" aria-hidden="true">
        <circle cx="12" cy="12" r="12" fill="var(--icon-bg)"/>
        <rect x="8.5" y="4.5" width="7" height="15" rx="1.5" fill="var(--brand-blue)"/>
        <rect x="9.8" y="6.5" width="4.4" height="6" fill="#ffffff"/>
      </svg>
      <span>239-555-0178</span>
    </div>

    <div class="contact-row contact-email">
      <svg class="contact-icon" viewBox="0 0 24 24" aria-hidden="true">
        <circle cx="12" cy="12" r="12" fill="var(--icon-bg)"/>
        <rect x="5" y="7.5" width="14" height="9.5" fill="var(--brand-blue)"/>
        <path d="M5 7.5 L12 13 L19 7.5" fill="none" stroke="#ffffff" stroke-width="1.3"/>
      </svg>
      <span>Marc@DorvelEng.com</span>
    </div>

    <div class="contact-row contact-web">
      <svg class="contact-icon" viewBox="0 0 24 24" aria-hidden="true">
        <circle cx="12" cy="12" r="12" fill="var(--icon-bg)"/>
        <g fill="none" stroke="var(--brand-blue)" stroke-width="1.4">
          <circle cx="12" cy="12" r="7"/>
          <ellipse cx="12" cy="12" rx="3" ry="7"/>
          <line x1="5" y1="12" x2="19" y2="12"/>
          <line x1="6" y1="8.5" x2="18" y2="8.5"/>
          <line x1="6" y1="15.5" x2="18" y2="15.5"/>
        </g>
      </svg>
      <span>www.DorvelEng.com</span>
    </div>

    <div class="footer-band"></div>
  </main>
</body>
</html>
```